依頼詳細
ページに使用したいキャッチフレーズ:
個性的な道を究め、劇的に生きる人生を選択する
それがMoonhollow

参考にしたいURL:
https://www.kenmori-ux.brelo.jp/
https://www.sorimachikeigo.com/member-lounge

ムーンホロウクラブのHP:
https://www.ruvo.co.jp/moonhollow/

ページに使用したいテキスト:
『Moonhollow Clubとは

「あなたの好きなことは何ですか?」
好きなことを徹底追求し、“好き”を個性に。
そして、個性を武器にしながら“才能”へと伸ばしていくことで、
人生の構想力が磨かれ、あなたの人生は切り拓かれていきます。

誰かに敷かれたレールに乗りたいのか?
型にはまらない人生を創造したいのか?
一度きりの人生を、自分はどう生きたいか?

「自分らしい」人生を実現しよう!。』

採択後、デザインに利用した、デザインデータもお送りください。
(特に、画像ファイルは必ず送ってください)

何かご不明な点がございましたら、お気軽にお申し付けください。

※ 過去の制作実績をそのままご提案いただいたり、他社のポートフォリオをそのまま掲載することは恐れ入りますが、ご遠慮いただけますと幸いです。
サイトURL
http://moonhollowclub.jp
ページ数
1ページ
希望イメージ
シンプル 複雑
単色 カラフル
暗い 明るい
日常 高級
遊び心 厳粛
未来的 伝統的
女性的 男性的
希望する色
赤系、黄・オレンジ系、ジェンダーニュートラルなデザイン
納品ファイル
• イラストレーター形式 (.ai)
• PNG形式 (.png)
補足説明
デザインに利用した、デザインデータ(画像など)もお送り頂きますようお願い致します。

素晴らしいデザインをありがとうございました。

素晴らしいデザインをありがとうございました。

```html
<!DOCTYPE html>
<html lang="ja">
<head>
<meta charset="utf-8">
<title>Moonhollow Club</title>
<link rel="stylesheet" href="https://fonts.googleapis.com/css2?family=Abril+Fatface&family=Montserrat:wght@600;800&family=Noto+Sans+JP:wght@400;500;700;900&display=swap">
<style>
:root{
  --yellow:#f2c04e;
  --blue:#4cb6e4;
  --ink:#222222;
  --dark:#363636;
  --white:#ffffff;
  --grey:#8a8a8a;
  --line:#d9d9d9;
}
*{box-sizing:border-box;margin:0;padding:0}
html,body{width:1200px;height:5160px;overflow:hidden}
body{position:relative;font-family:"Noto Sans JP",sans-serif;color:var(--ink);background:var(--white)}
.abs{position:absolute}
.display{font-family:"Abril Fatface",serif;font-weight:400}
.latin{font-family:"Montserrat",sans-serif}
.photo{position:absolute;border-radius:16px}

/* header */
.topbar{position:absolute;left:0;top:0;width:1200px;height:52px;z-index:3;display:flex;align-items:center;justify-content:center}
.topbar .menu{position:absolute;left:60px;top:22px;width:26px;height:3px;background:var(--ink)}
.topbar .brand{font-family:"Montserrat",sans-serif;font-weight:800;font-size:20px}
.topbar .auth{position:absolute;right:40px;font-size:14px;font-weight:500}

/* hero */
.hero{position:absolute;left:0;top:0;width:1200px;height:680px;background:linear-gradient(180deg,#efeae2 0%,#d8d2c7 30%,#b9ac98 55%,#6d6150 80%,#3e362c 100%)}
.hero-title{position:absolute;left:56px;top:150px;color:var(--white);font-size:140px;line-height:140px;white-space:nowrap}
.hero-copy{position:absolute;left:420px;top:500px;color:var(--white);font-size:24px;font-weight:700;line-height:1.5;letter-spacing:.04em}

/* intro */
.intro{position:absolute;left:0;top:680px;width:1200px;height:900px;background:var(--yellow);overflow:hidden}
.corner{position:absolute;width:80px;height:80px;border:6px solid var(--white)}
.corner.tl{left:20px;top:20px;border-right:none;border-bottom:none}
.corner.tr{right:20px;top:20px;border-left:none;border-bottom:none}
.corner.bl{left:20px;bottom:40px;border-right:none;border-top:none}
.corner.br{right:20px;bottom:40px;border-left:none;border-top:none}
.ghost{position:absolute;left:-120px;top:340px;font-size:150px;color:rgba(255,255,255,.22);white-space:nowrap}
.intro-text{position:absolute;left:0;top:150px;width:1200px;text-align:center;color:var(--white);font-size:22px;font-weight:500;line-height:46px}
.intro-text p+p{margin-top:34px}
.intro-cta{position:absolute;left:0;top:700px;width:1200px;text-align:center}
.intro-cta span{color:var(--white);font-size:36px;font-weight:900;letter-spacing:.04em;padding:0 8px 6px;border-bottom:10px solid var(--blue)}

/* section heads */
.sec-title{font-size:92px;line-height:1}
.sec-rule{height:4px;background:var(--ink)}
.sec-sub{font-size:20px;font-weight:700}
.more{display:flex;align-items:center;gap:28px;font-family:"Montserrat",sans-serif;font-weight:800;font-size:22px}
.circle{width:92px;height:92px;border-radius:50%;display:flex;align-items:center;justify-content:center}

/* movie */
.tag{display:inline-block;background:var(--blue);color:var(--white);font-size:13px;font-weight:700;padding:4px 14px;border-radius:14px}
.meta{position:absolute;display:flex;align-items:center;justify-content:space-between;border-bottom:2px solid var(--line);padding-bottom:12px}
.meta .date{font-family:"Montserrat",sans-serif;font-weight:800;font-size:18px}
.meta .name{font-weight:700;font-size:18px}
.meta.small .date,.meta.small .name{font-size:14px}
.meta.small .tag{font-size:11px;padding:3px 10px}
.pill-on{position:absolute;left:16px;top:14px}

/* blog */
.blog-band{position:absolute;left:0;top:2820px;width:1200px;height:380px;background:var(--yellow)}
.card{position:absolute;top:3040px;width:350px;height:300px;background:var(--white);border-radius:14px;box-shadow:8px 10px 0 rgba(0,0,0,.08),0 6px 18px rgba(0,0,0,.1);overflow:hidden}
.card .img{height:170px}
.card .row{display:flex;justify-content:space-between;align-items:center;padding:18px 22px 0}
.card .date{font-family:"Montserrat",sans-serif;font-weight:600;font-size:15px}
.card .title{padding:18px 22px 0;font-weight:700;font-size:20px}

/* chat */
.chat{position:absolute;left:56px;top:3528px;width:1100px;height:330px;border:4px solid var(--blue);border-radius:14px;background:var(--white);box-shadow:12px 14px 0 var(--blue)}
.chat-note{position:absolute;left:640px;top:92px;font-size:21px;font-weight:700;line-height:1.7;text-align:center}
.chat-note em{font-style:normal;color:var(--blue)}
.search{position:absolute;left:640px;top:200px;width:380px;height:56px;border-radius:28px;background:var(--white);box-shadow:0 4px 12px rgba(0,0,0,.15)}

/* membership */
.member{position:absolute;left:0;top:4000px;width:1200px;height:540px;background:linear-gradient(120deg,#5b4f45 0%,#a88a63 45%,#e9c488 62%,#7a6550 80%,#4a3f38 100%)}
.member-title{position:absolute;left:118px;top:60px;color:var(--white);font-size:118px;line-height:.95}
.join{position:absolute;left:120px;top:368px;width:480px;height:112px;border-radius:10px;background:var(--blue);color:var(--white);display:flex;align-items:center;justify-content:center;gap:70px;font-size:28px;font-weight:700}

/* footer */
.footer{position:absolute;left:0;top:4540px;width:1200px;height:620px;background:var(--dark);color:var(--white);overflow:hidden}
.fnav{position:absolute;left:56px;top:80px}
.fnav li{list-style:none;display:flex;align-items:baseline;gap:12px;margin-bottom:24px}
.fnav b{font-family:"Montserrat",sans-serif;font-weight:800;font-size:38px;color:var(--yellow)}
.fnav span{font-size:17px}
.totop{position:absolute;left:900px;top:20px;width:260px;height:260px;border-radius:50%;background:var(--yellow);display:flex;align-items:center;justify-content:center}
.flinks{position:absolute;left:56px;top:318px;width:1088px;display:flex;justify-content:space-between;font-size:15px;padding-bottom:14px;border-bottom:2px solid rgba(255,255,255,.5)}
.flinks .right{display:flex;gap:48px}
.fbig{position:absolute;left:0;top:400px;width:1200px;text-align:center;font-size:116px;color:var(--yellow);line-height:1.2;white-space:nowrap}
.fbottom{position:absolute;left:56px;top:572px;width:1088px;display:flex;justify-content:space-between;color:var(--yellow);font-size:16px;font-weight:700}
.fbottom .latin{font-size:14px}
</style>
</head>
<body>

<section class="hero" role="img" aria-label="霧の中へ続く線路の写真"></section>
<header class="topbar">
  <div class="menu"></div>
  <div class="brand">Moonhollow Club</div>
  <div class="auth">Login / 会員登録</div>
</header>
<h1 class="hero-title display">Moon<br>hollow<br>Club</h1>
<p class="hero-copy">個性的な道を究め、<br>劇的に生きる人生を選択する<br>それがMoonhollow</p>

<section class="intro">
  <div class="corner tl"></div><div class="corner tr"></div>
  <div class="corner bl"></div><div class="corner br"></div>
  <div class="ghost display">What Moonhollow Club</div>
  <div class="intro-text">
    <p>「あなたの好きなことは何ですか？」<br>好きなことを徹底追求し、“好き”を個性に。<br>そして、個性を武器にしながら<br>“才能”へと伸ばしていくことで、<br>人生の構想力が磨かれ、<br>あなたの人生は切り拓かれていきます。</p>
    <p>誰かに敷かれたレールに乗りたいのか？<br>型にはまらない人生を創造したいのか？<br>一度きりの人生を、自分はどう生きたいか？</p>
  </div>
  <div class="intro-cta"><span>「自分らしい」人生を実現しよう！</span></div>
</section>

<!-- movie -->
<h2 class="abs display sec-title" style="left:120px;top:1720px">Movie</h2>
<div class="abs sec-rule" style="left:120px;top:1822px;width:220px"></div>
<div class="abs sec-sub" style="left:120px;top:1836px">新着動画</div>
<div class="abs more" style="left:120px;top:1908px">View More
  <div class="circle" style="background:var(--yellow)"><svg width="34" height="20" viewBox="0 0 34 20"><path d="M0 10h30M22 2l8 8-8 8" fill="none" stroke="#fff" stroke-width="3"/></svg></div>
</div>

<div class="photo" style="left:460px;top:1720px;width:680px;height:380px;background:linear-gradient(135deg,#c9ccc9,#8f9596 55%,#5f5a55)" role="img" aria-label="対談する二人の写真"></div>
<div class="meta" style="left:460px;top:2124px;width:680px"><span class="tag">セミナー</span><span style="flex:1"></span><span class="date">2022.12.16</span><span class="name" style="margin-left:40px">写真サンプル01</span></div>

<div class="photo" style="left:460px;top:2228px;width:310px;height:172px;background:linear-gradient(135deg,#6e5548,#c7a27a)" role="img" aria-label="会話する二人の写真"><span class="tag pill-on">セミナー</span></div>
<div class="meta small" style="left:460px;top:2412px;width:310px"><span class="date">2022.12.16</span><span class="name">写真サンプル02</span></div>
<div class="photo" style="left:830px;top:2228px;width:310px;height:172px;background:linear-gradient(135deg,#1d2c44,#3f6a9a)" role="img" aria-label="光を手にする人物の写真"><span class="tag pill-on">セミナー</span></div>
<div class="meta small" style="left:830px;top:2412px;width:310px"><span class="date">2022.12.16</span><span class="name">写真サンプル03</span></div>
<div class="photo" style="left:460px;top:2480px;width:310px;height:172px;background:linear-gradient(135deg,#d6d6d2,#9aa58c)" role="img" aria-label="並んだ椅子の写真"><span class="tag pill-on">セミナー</span></div>
<div class="meta small" style="left:460px;top:2664px;width:310px"><span class="date">2022.12.16</span><span class="name">写真サンプル04</span></div>
<div class="photo" style="left:830px;top:2480px;width:310px;height:172px;background:linear-gradient(135deg,#2c3a4c,#8d8f95)" role="img" aria-label="話し合う二人の写真"><span class="tag pill-on">セミナー</span></div>
<div class="meta small" style="left:830px;top:2664px;width:310px"><span class="date">2022.12.16</span><span class="name">写真サンプル05</span></div>

<!-- blog -->
<div class="blog-band"></div>
<h2 class="abs display sec-title" style="left:120px;top:2880px">Blog</h2>
<div class="abs sec-rule" style="left:120px;top:2980px;width:180px"></div>
<div class="abs sec-sub" style="left:318px;top:2928px;font-weight:500">ブログ</div>
<div class="abs more" style="left:850px;top:2900px">View More
  <div class="circle" style="background:var(--white)"><svg width="34" height="20" viewBox="0 0 34 20"><path d="M0 10h30M22 2l8 8-8 8" fill="none" stroke="#222" stroke-width="3"/></svg></div>
</div>

<article class="card" style="left:120px"><div class="img" style="background:linear-gradient(180deg,#f4f4f4,#dcdcdc)" role="img" aria-label="ウェブ画面の画像"></div><div class="row"><span class="date">2023.01.10</span><span class="tag">コラム</span></div><div class="title">まずは己の力を知るべし</div></article>
<article class="card" style="left:508px"><div class="img" style="background:linear-gradient(180deg,#f3d98a,#b88a4c 60%,#5f4a33)" role="img" aria-label="光に照らされた線路の写真"></div><div class="row"><span class="date">2023.01.10</span><span class="tag">コラム</span></div><div class="title">まずは己の力を知るべし</div></article>
<article class="card" style="left:892px"><div class="img" style="background:linear-gradient(180deg,#8fb8de,#c9b48c 60%,#6a5a48)" role="img" aria-label="まっすぐ続く道路の写真"></div><div class="row"><span class="date">2023.01.10</span><span class="tag">コラム</span></div><div class="title">まずは己の力を知るべし</div></article>

<!-- chat -->
<section class="chat">
  <h2 class="abs display" style="left:60px;top:92px;font-size:78px;line-height:1">Chat Room</h2>
  <div class="abs sec-rule" style="left:60px;top:182px;width:410px"></div>
  <div class="abs sec-sub" style="left:60px;top:196px">掲示板</div>
  <p class="chat-note">チャットルームを利用する場合は、<br><em>ログイン</em>してください</p>
  <div class="search"><svg style="position:absolute;right:24px;top:16px" width="24" height="24" viewBox="0 0 24 24"><circle cx="10" cy="10" r="7" fill="none" stroke="#222" stroke-width="3"/><path d="M15 15l7 7" stroke="#222" stroke-width="3"/></svg></div>
</section>

<!-- membership -->
<section class="member" role="img" aria-label="夕日の中で手でフレームを作る人物の写真">
  <h2 class="member-title display">Member<br>ship</h2>
  <div class="join">会員登録
    <svg width="52" height="52" viewBox="0 0 52 52"><circle cx="26" cy="26" r="24" fill="none" stroke="#fff" stroke-width="3"/><path d="M16 26h19M29 19l7 7-7 7" fill="none" stroke="#fff" stroke-width="3"/></svg>
  </div>
</section>

<!-- footer -->
<footer class="footer">
  <ul class="fnav">
    <li><b>HOME</b><span>ホーム</span></li>
    <li><b>Membership</b><span>会員登録</span></li>
    <li><b>Contact</b><span>お問い合わせ</span></li>
  </ul>
  <div class="totop"><svg width="90" height="110" viewBox="0 0 90 110"><path d="M45 105V8M8 45L45 8l37 37" fill="none" stroke="#363636" stroke-width="7"/></svg></div>
  <div class="flinks"><span>アンケート</span><span class="right"><span>個人情報保護方針</span><span>利用規約</span><span>特定商取引法に基づく表記</span></span></div>
  <div class="fbig display">Moonhollow Club</div>
  <div class="fbottom"><span>個性的な道を究め、劇的に生きる</span><span class="latin">Copyright ©2022 Moonhollow Club All Rights Reserved.</span></div>
</footer>

</body>
</html>
```